Ridgeline Wild Craft DL flyer

I'm looking for a new flyer for my startup business. In Darwin Australia.
Aimed at family's and short stay tourists the "Ridgeline Wild Craft" 4 hr tour will give people a basic understanding of some essential bush survival skills in the Australian Outback.
things covered in this 4 hr tour are
1. Finding water.
2. finding food.
3. Finding/making shelter and fire.
4. Finding your way home.

The tour will pick clients up in an air conditioned purpose build 4WD and take them to a nearby bushland area where they will have the opportunity to catch and harvest some native bushtucker.
They will then be able to find/harvest some water for survival situations.
While we cook our bush tucker they will also learn to find their way home through ancient navigation techniques as well.

Clients will then be dropped back to their accomodation with some fun and vital knowledge of surviving in the Australian outback.
At the end of the tour the group will be able to take home a basic survival kit which they will be able to use through the skills they just gained on the tour.

I'd like a two sided DL size flyer emphasising the following points.
4hr/half day tour
Fun for the family
Free survival kit included.
Eat what you catch
Learn essential survival skills
Provided buy an experienced and passionate bushman.
$150/head including transfers.

I'll provide some pictures for the flyer and any extra content you require.

Target Market(s)

Family's
Short stay tourists

Industry/Entity Type

Tourism

Colors

Designer to choose colors to be used in the design.

Requirements
Must have
• As per brief
Nice to have
• Any extra content and flair designers would like to add
Should not have
• Any images which aren't Australian

```html
<!DOCTYPE html>
<html lang="en">
<head>
<meta charset="utf-8">
<title>Ridgeline Wild Craft – DL Flyer</title>
<link href="https://fonts.googleapis.com/css2?family=Roboto+Condensed:wght@700&family=Open+Sans:wght@400;600&display=swap" rel="stylesheet">
<style>
:root{
  --red:#e30613;
  --red-dark:#c8050f;
  --pink:#ec5860;
  --charcoal:#3d3d3d;
  --white:#ffffff;
  --page:#ececec;
  --leaf:#4f7d34;
  --sand:#b9a58c;
}
*{margin:0;padding:0;box-sizing:border-box}
html,body{width:1200px;height:1000px;overflow:hidden;background:var(--page)}
.canvas{position:relative;width:1200px;height:1000px}
.flyer{position:absolute;top:95px;width:404px;height:808px;background:var(--charcoal);overflow:hidden;font-family:"Open Sans",Arial,sans-serif;color:var(--white);box-shadow:0 3px 8px rgba(0,0,0,.35)}
.flyer--front{left:155px}
.flyer--back{left:641px}
.flyer__header{height:93px;background:var(--red);display:flex;align-items:center;justify-content:center}
.flyer__title{font-family:"Roboto Condensed","Arial Narrow",sans-serif;font-weight:700;font-size:32px;text-shadow:0 2px 2px rgba(0,0,0,.3)}
.photo{display:block;width:100%}
.photo--water-bag{height:212px;background:linear-gradient(160deg,#1d3a1e 0%,#3f6e2c 40%,#c9d3cf 55%,#6ea041 75%,#5a8e35 100%)}
.photo--bush-fruit{height:210px;background:linear-gradient(135deg,#c7b6a6 0%,#d9c3b4 35%,#8fa04a 55%,#b7a596 80%,#a89889 100%)}
.body-copy{padding:7px 17px 0 17px;font-size:12px;line-height:16px;text-align:justify}
.flyer--back .body-copy{padding-top:23px}
.body-copy p+p{margin-top:0}
.body-copy .gap{margin-top:10px}
.skills{display:flex;height:92px;margin-top:6px}
.skill{flex:1;display:flex;flex-direction:column;align-items:center;justify-content:flex-end;padding-bottom:8px;font-size:12px;line-height:16px;text-align:center}
.skill:nth-child(odd){background:var(--red)}
.skill:nth-child(even){background:var(--pink)}
.skill svg{margin-bottom:auto;margin-top:14px}
.services-btn{display:block;width:140px;height:31px;margin:11px auto 0;border-radius:5px;background:linear-gradient(#f3313b,var(--red-dark));font-size:15px;line-height:31px;text-align:center;letter-spacing:.3px;box-shadow:0 2px 2px rgba(0,0,0,.35)}
.services{list-style:none;position:absolute;left:17px;top:576px;font-size:12px;line-height:16px}
.services li{position:relative;padding-left:18px;margin-bottom:4px}
.services li svg{position:absolute;left:0;top:2px}
.circle-photo{position:absolute;border-radius:50%;border:3px solid var(--white)}
.footer-shape{position:absolute;left:0;bottom:0}
.call{position:absolute;right:13px;bottom:13px;text-align:right;font-family:"Roboto Condensed","Arial Narrow",sans-serif;font-weight:700;line-height:1}
.call__label{font-size:23px;display:block;margin-bottom:6px}
.call__number{font-size:33px;display:block}
.site{position:absolute;left:28px;bottom:6px;font-size:12px;display:flex;align-items:center;gap:5px}
.site__dot{width:10px;height:10px;border:2px solid var(--white);border-radius:50%}
</style>
</head>
<body>
<div class="canvas">

  <section class="flyer flyer--front">
    <header class="flyer__header"><h1 class="flyer__title">Ridgeline Wild Craft</h1></header>
    <div class="photo photo--water-bag" role="img" aria-label="Clear plastic bag tied over a leafy branch collecting water on green grass"></div>
    <div class="body-copy">
      <p>The tour will pick clients up in an air conditioned purpose build 4WD and take them to a nearby bushland area where they will have the opportunity to catch and harvest some native bushtucker.</p>
      <p>They will then be able to find/harvest some water for survival situations.</p>
      <p>While we cook our bush tucker they will also learn to find their way home through ancient navigation techniques as well.</p>
    </div>
    <div class="skills">
      <div class="skill">
        <svg width="22" height="30" viewBox="0 0 22 30"><path d="M11 1C8 9 2 14 2 20a9 9 0 0 0 18 0c0-6-6-11-9-19z" fill="#fff"/></svg>
        <span>Finding water</span>
      </div>
      <div class="skill">
        <svg width="44" height="34" viewBox="0 0 44 34"><circle cx="24" cy="5" r="2.5" fill="#fff"/><path d="M10 20a14 12 0 0 1 28 0z" fill="#fff"/><rect x="7" y="21" width="34" height="3" rx="1.5" fill="#fff"/><path d="M2 26h10l8 4h14v3H18l-8-3H2z" fill="#fff"/></svg>
        <span>Finding Food</span>
      </div>
      <div class="skill">
        <svg width="44" height="34" viewBox="0 0 44 34"><path d="M22 3l11 9v11H11V12z" fill="#fff"/><rect x="19" y="15" width="6" height="8" fill="#e30613"/><path d="M2 14c3 8 8 14 16 18M42 14c-3 8-8 14-16 18" stroke="#fff" stroke-width="3" fill="none" stroke-linecap="round"/></svg>
        <span>Finding/Making<br>Shelter and Fire</span>
      </div>
      <div class="skill">
        <svg width="40" height="32" viewBox="0 0 40 32"><path d="M20 2L2 17h5v14h9v-9h8v9h9V17h5z" fill="#fff"/></svg>
        <span>Finding your<br>way Home</span>
      </div>
    </div>
    <span class="services-btn">OUR SERVICES</span>
    <ul class="services">
      <li><svg width="12" height="11" viewBox="0 0 12 11"><path d="M1 6l3 4 7-9" stroke="#e30613" stroke-width="2" fill="none"/></svg>4hr/half day tour</li>
      <li><svg width="12" height="11" viewBox="0 0 12 11"><path d="M1 6l3 4 7-9" stroke="#e30613" stroke-width="2" fill="none"/></svg>Fun for the family</li>
      <li><svg width="12" height="11" viewBox="0 0 12 11"><path d="M1 6l3 4 7-9" stroke="#e30613" stroke-width="2" fill="none"/></svg>Free survival kit included</li>
      <li><svg width="12" height="11" viewBox="0 0 12 11"><path d="M1 6l3 4 7-9" stroke="#e30613" stroke-width="2" fill="none"/></svg>Eat what you catch</li>
      <li><svg width="12" height="11" viewBox="0 0 12 11"><path d="M1 6l3 4 7-9" stroke="#e30613" stroke-width="2" fill="none"/></svg>Learn essential survival skills</li>
      <li><svg width="12" height="11" viewBox="0 0 12 11"><path d="M1 6l3 4 7-9" stroke="#e30613" stroke-width="2" fill="none"/></svg>Provided buy an experienced<br>and passionate bushman</li>
      <li><svg width="12" height="11" viewBox="0 0 12 11"><path d="M1 6l3 4 7-9" stroke="#e30613" stroke-width="2" fill="none"/></svg>$150/head including transfers</li>
    </ul>
    <div class="circle-photo" style="left:212px;top:587px;width:84px;height:84px;background:linear-gradient(135deg,#8a7a6a,#c9a88a 60%,#5c6e7a)" role="img" aria-label="Hands holding a freshly caught yabby"></div>
    <div class="circle-photo" style="left:293px;top:587px;width:84px;height:84px;background:linear-gradient(180deg,#9fb9d0,#6d8a4a 55%,#8a5a3a)" role="img" aria-label="Outback bushland with red earth and trees"></div>
    <div class="circle-photo" style="left:260px;top:635px;width:92px;height:92px;background:linear-gradient(160deg,#6f8f4c,#b08d6c 60%,#4a5a3a)" role="img" aria-label="Bushman holding bush tucker outdoors"></div>
    <svg class="footer-shape" width="404" height="120" viewBox="0 0 404 120"><polygon points="0,77 404,8 404,120 0,120" fill="var(--red)"/><polygon points="0,32 82,77 0,77" fill="var(--pink)"/></svg>
    <div class="call"><span class="call__label">CALL NOW</span><span class="call__number">0400 218 563</span></div>
    <div class="site"><span class="site__dot"></span>www.ridgelinewild.com.au</div>
  </section>

  <section class="flyer flyer--back">
    <header class="flyer__header"><h1 class="flyer__title">Ridgeline Wild Craft</h1></header>
    <div class="photo photo--bush-fruit" role="img" aria-label="Open hand holding small green native bush fruits with fine hairy husks"></div>
    <div class="body-copy">
      <p>Clients will then be dropped back to their accomodation with some fun and vital knowledge of surviving in the Australian outback.</p>
      <p>At the end of the tour the group will be able to take home a basic survival kit which they will be able to use through the skills they just gained on the tour.</p>
      <p class="gap">Lorem Ipsum is simply dummy text of the printing and typesetting industry. Lorem Ipsum has been the industry's standard dummy text ever since the 1500s, when an unknown printer took a galley of type and scrambled it to make a type specimen book. It has survived not only five centuries, but also the leap into electronic typesetting, remaining essentially unchanged. It was popularised in the 1960s with the release of Letraset sheets containing Lorem Ipsum passages, and more recently with desktop publishing software like Aldus PageMaker including versions of Lorem Ipsum.</p>
    </div>
    <div class="circle-photo" style="left:46px;top:605px;width:94px;height:94px;background:linear-gradient(160deg,#8fb3d6,#7a5a3e 55%,#c9852f)" role="img" aria-label="Branch with native fruit against the sky"></div>
    <div class="circle-photo" style="left:136px;top:580px;width:136px;height:136px;background:linear-gradient(135deg,#a58a6c,#c4a98a 50%,#8d7357)" role="img" aria-label="Stick and seeds laid on sandy ground"></div>
    <div class="circle-photo" style="left:262px;top:601px;width:98px;height:98px;background:radial-gradient(circle,#d8e0c0,#5f8a3a 55%,#3e6028)" role="img" aria-label="Spiky native palm fronds"></div>
    <svg class="footer-shape" width="404" height="120" viewBox="0 0 404 120"><polygon points="0,77 404,8 404,120 0,120" fill="var(--red)"/><polygon points="0,32 82,77 0,77" fill="var(--pink)"/></svg>
    <div class="call"><span class="call__label">CALL NOW</span><span class="call__number">0400 218 563</span></div>
    <div class="site"><span class="site__dot"></span>www.ridgelinewild.com.au</div>
  </section>

</div>
</body>
</html>
```